Three diagrams for research framework required

I need a three diagrams produced to capture principles of a research approach.<br/><br/>The first is a cycle diagram, produced to capture seven principles of a research framework. My idea is to be similar to the example attached, but incorporate seven principles and the koru (fern) imagery (example attached) that relates to our logo (also attached). The centre piece of the diagram should be labelled Open Trail Reading Method.<br/><br/>The seven principles are:<br/>1. Thinking proactively<br/>2. Ensuring positive learning experiences<br/>3. Fostering positive collaborations<br/>4. Providing constructive reporting<br/>5. Prioritising whānau engagement<br/>6. Being culturally responsive<br/>7. Maximizing protective factors<br/><br/>The second and third diagram should be updated versions of the attached, so all three diagrams look related. See diagrams attached that require updating (diagram 2 and 3).<br/><br/>The three diagrams need to be cohesive and clearly related aesthetically. All final files need to be produced in Adobe Photoshop or InDesign, so minor edits to text can easily be made in future.

Industry/Entity Type

Education

Font styles to use
Sans Serif

Colors

Designer to choose colors to be used in the design.

Requirements
Must have
• Clean design, easy to read and understand.
Should not have
• Complicated, overly busy design.

```html
<!DOCTYPE html>
<html lang="en">
<head>
<meta charset="utf-8">
<title>Open Trail Reading Method – Seven Principles</title>
<link rel="stylesheet" href="https://fonts.googleapis.com/css2?family=Fjalla+One&display=swap">
<style>
  :root {
    --paper: #efeff0;
    --swirl-grey: #d2d2d4;
    --leaf-green: #6b9c35;
    --leaf-green-edge: #3f6c1e;
    --berry: #5c0a29;
    --berry-edge: #3a0418;
    --ink: #141414;
    --light-text: #ffffff;
    --hub-ring: #c9c9cc;
  }
  html, body {
    margin: 0;
    padding: 0;
    width: 1180px;
    height: 1200px;
    overflow: hidden;
    background: var(--paper);
  }
  .framework-poster {
    display: block;
    width: 1180px;
    height: 1200px;
    font-family: "Fjalla One", "Arial Narrow", sans-serif;
  }
  .swirl-backdrop { fill: var(--swirl-grey); }
  .principle--green .petal { fill: var(--leaf-green); stroke: var(--leaf-green-edge); }
  .principle--berry .petal { fill: var(--berry); stroke: var(--berry-edge); }
  .petal { stroke-width: 5; stroke-linejoin: round; }
  .principle-number { font-size: 44px; text-anchor: middle; }
  .principle-label { font-size: 13px; text-anchor: middle; letter-spacing: 0.2px; }
  .principle-rule { stroke-width: 1.4; stroke-dasharray: 4 2.5; }
  .principle--green text { fill: var(--ink); }
  .principle--green .principle-rule { stroke: var(--ink); }
  .principle--berry text { fill: var(--light-text); }
  .principle--berry .principle-rule { stroke: var(--light-text); }
  .hub-ring { fill: var(--hub-ring); }
  .hub-disc { fill: #ffffff; }
  .hub-name { fill: var(--berry); font-size: 19px; text-anchor: middle; }
  .poster-title { fill: var(--ink); font-size: 78px; letter-spacing: -0.5px; }
</style>
</head>
<body>
<svg class="framework-poster" viewBox="0 0 1180 1200" role="img" aria-label="Open Trail Reading Method: seven principles cycle diagram">
  <defs>
    <path id="petal-shape" d="M99.4,-42.2 C135,-58 235,-52 261.4,-18.3 C285,30 262,145 191.7,178.7 C198.3,136.4 134.5,59.2 98.7,43.9 A108,108 0 0 0 99.4,-42.2 Z"/>
  </defs>

  <g transform="translate(590,0) scale(1.166) translate(-700,-233)">
    <path class="swirl-backdrop" d="M700,325 A323,323 0 0 1 1005,770 C965,845 932,920 962,1000 C992,1080 1060,1140 1210,1200 L1210,1262 L1060,1262 C900,1150 760,1060 620,1000 C470,930 378,800 378,650 A322,322 0 0 1 700,325 Z"/>

    <g class="principles" transform="translate(700,648)">
      <g class="principle principle--green"><use class="petal" href="#petal-shape" transform="rotate(-95.6)"/></g>
      <g class="principle principle--berry"><use class="petal" href="#petal-shape" transform="rotate(-44.2)"/></g>
      <g class="principle principle--berry"><use class="petal" href="#petal-shape" transform="rotate(7.3)"/></g>
      <g class="principle principle--berry"><use class="petal" href="#petal-shape" transform="rotate(58.7)"/></g>
      <g class="principle principle--green"><use class="petal" href="#petal-shape" transform="rotate(110.1)"/></g>
      <g class="principle principle--green"><use class="petal" href="#petal-shape" transform="rotate(161.6)"/></g>
      <g class="principle principle--green"><use class="petal" href="#petal-shape" transform="rotate(213)"/></g>
    </g>

    <g class="principle principle--green">
      <text class="principle-number" x="708" y="443">1</text>
      <line class="principle-rule" x1="672" y1="455" x2="744" y2="455"/>
      <text class="principle-label" x="708" y="475">THINKING</text>
      <text class="principle-label" x="708" y="492">PROACTIVELY</text>
    </g>
    <g class="principle principle--berry">
      <text class="principle-number" x="866" y="528">2</text>
      <line class="principle-rule" x1="808" y1="541" x2="924" y2="541"/>
      <text class="principle-label" x="866" y="561">ENSURING POSITIVE</text>
      <text class="principle-label" x="866" y="578">LEARNING EXPERIENCES</text>
    </g>
    <g class="principle principle--berry">
      <text class="principle-number" x="886" y="692">3</text>
      <line class="principle-rule" x1="834" y1="705" x2="948" y2="705"/>
      <text class="principle-label" x="892" y="725">FOSTERING POSITIVE</text>
      <text class="principle-label" x="892" y="742">COLLABORATIONS</text>
    </g>
    <g class="principle principle--berry">
      <text class="principle-number" x="767" y="812">4</text>
      <line class="principle-rule" x1="734" y1="826" x2="806" y2="826"/>
      <text class="principle-label" x="770" y="847">PROVIDING</text>
      <text class="principle-label" x="770" y="864">CONSTRUCTIVE</text>
      <text class="principle-label" x="770" y="881">REPORTING</text>
    </g>
    <g class="principle principle--green">
      <text class="principle-number" x="602" y="806">5</text>
      <line class="principle-rule" x1="562" y1="816" x2="644" y2="816"/>
      <text class="principle-label" x="604" y="835">PRIORITISING</text>
      <text class="principle-label" x="604" y="852">WHĀNAU</text>
      <text class="principle-label" x="604" y="869">ENGAGEMENT</text>
    </g>
    <g class="principle principle--green">
      <text class="principle-number" x="502" y="668">6</text>
      <line class="principle-rule" x1="458" y1="680" x2="560" y2="680"/>
      <text class="principle-label" x="508" y="697">BEING CULTURALLY</text>
      <text class="principle-label" x="508" y="714">RESPONSIVE</text>
    </g>
    <g class="principle principle--green">
      <text class="principle-number" x="560" y="495">7</text>
      <line class="principle-rule" x1="522" y1="510" x2="598" y2="510"/>
      <text class="principle-label" x="560" y="528">MAXIMIZING</text>
      <text class="principle-label" x="560" y="545">PROTECTIVE</text>
      <text class="principle-label" x="560" y="562">FACTORS</text>
    </g>

    <g class="hub">
      <circle class="hub-ring" cx="700" cy="648" r="104"/>
      <circle class="hub-disc" cx="700" cy="648" r="97"/>
      <text class="hub-name" x="700" y="630">OPEN TRAIL</text>
      <text class="hub-name" x="700" y="656">READING</text>
      <text class="hub-name" x="700" y="682">METHOD</text>
    </g>

    <g class="poster-title">
      <text x="348" y="1012">OPEN</text>
      <text x="348" y="1084">TRAIL</text>
      <text x="348" y="1156">READING</text>
      <text x="348" y="1228">METHOD</text>
    </g>
  </g>
</svg>
</body>
</html>
```